Business Card Design

I have just recently added a towing service to my automobile repair business. I have a logo and would like to know what it would look like with my logo and a picture of my tow truck on the business card, with the address and phone number included.

I'm having trouble uploading my truck photo. I can email it to you if you give me an address.

Industry/Entity Type

Business

Contact Information for Business Card

Hollister's towing, service & repair
4718 NW St. Rt. K
Brayfield, Mo. 63518
555-384-7201

Colors
3277b5
85acd2
cedeec

```html
<!DOCTYPE html>
<html lang="en">
<head>
<meta charset="utf-8">
<title>Business Card – Hollister's Towing, Service & Repair</title>
<link href="https://fonts.googleapis.com/css2?family=Open+Sans:wght@300;400;600&display=swap" rel="stylesheet">
<style>
  :root {
    --brand-blue: #3277b5;
    --mid-blue: #85acd2;
    --pale-blue: #cedeec;
    --ink: #2b2b2b;
    --card: #ffffff;
    --stage: #ece9e4;
  }
  html, body {
    margin: 0;
    width: 1200px;
    height: 1023px;
    overflow: hidden;
    background: var(--stage);
    font-family: "Open Sans", Arial, sans-serif;
  }
  .business-card {
    position: absolute;
    left: 150px;
    top: 254px;
    width: 900px;
    height: 514px;
    background: var(--card);
    box-shadow: 0 10px 30px rgba(0,0,0,0.18);
    overflow: hidden;
  }
  .truck-photo {
    position: absolute;
    inset: 0 0 52px 0;
    background: linear-gradient(100deg, #f7f8fa 0%, #eceff3 40%, #f1f3f6 70%, #fafbfc 100%);
  }
  .logo-panel {
    position: absolute;
    left: 70px;
    top: 150px;
    width: 290px;
    height: 170px;
    background: rgba(255,255,255,0.85);
    display: flex;
    align-items: center;
    justify-content: center;
    gap: 12px;
  }
  .logo-mark {
    width: 22px;
    height: 22px;
    background: var(--brand-blue);
  }
  .logo-name {
    font-size: 36px;
    font-weight: 600;
    color: var(--brand-blue);
  }
  .contact-block {
    position: absolute;
    left: 420px;
    top: 76px;
  }
  .person-name {
    margin: 0;
    font-size: 36px;
    font-weight: 600;
    color: var(--brand-blue);
    line-height: 1.15;
  }
  .person-title {
    margin: 0;
    font-size: 28px;
    font-weight: 300;
    color: var(--ink);
    line-height: 1.2;
  }
  .divider {
    position: absolute;
    left: 300px;
    top: 180px;
    width: 330px;
    height: 2px;
    background: linear-gradient(90deg, rgba(50,119,181,0) 0%, var(--brand-blue) 60%, var(--mid-blue) 100%);
  }
  .address {
    margin: 56px 0 0;
    font-size: 20px;
    font-weight: 400;
    color: var(--ink);
    line-height: 1.35;
  }
  .contact-line {
    display: flex;
    align-items: center;
    gap: 10px;
    font-size: 20px;
    color: var(--ink);
    line-height: 1.6;
  }
  .contact-line svg { flex: none; }
  .edge-band-light {
    position: absolute;
    left: 0; right: 0;
    bottom: 40px;
    height: 12px;
    background: var(--pale-blue);
  }
  .edge-band {
    position: absolute;
    left: 0; right: 0;
    bottom: 0;
    height: 40px;
    background: var(--brand-blue);
  }
</style>
</head>
<body>
  <div class="business-card">
    <div class="truck-photo" role="img" aria-label="Faint photo of the company tow truck"></div>

    <div class="logo-panel">
      <span class="logo-mark"></span>
      <span class="logo-name">Hollister's</span>
    </div>

    <div class="divider"></div>

    <div class="contact-block">
      <h1 class="person-name">Hollis Brenner</h1>
      <p class="person-title">Director</p>
      <p class="address">Hollister's towing, service &amp; repair<br>4718 NW St. Rt. K Brayfield,</p>
      <div class="contact-line">
        <svg width="16" height="18" viewBox="0 0 16 18" aria-hidden="true"><rect x="2" y="1" width="12" height="16" rx="2" fill="none" stroke="#2b2b2b" stroke-width="1.6"/></svg>
        <span>63518 555-384-7201</span>
      </div>
      <div class="contact-line">
        <svg width="18" height="14" viewBox="0 0 18 14" aria-hidden="true"><rect x="1" y="1" width="16" height="12" fill="#3277b5"/><path d="M1 1 L9 8 L17 1" fill="none" stroke="#fff" stroke-width="1.4"/></svg>
        <span>hollisbrenner@mailbox.com</span>
      </div>
    </div>

    <div class="edge-band-light"></div>
    <div class="edge-band"></div>
  </div>
</body>
</html>
```